dessert restaurant

I need a business card design for my restaurant. It will primarily be a dessert and wine restaurant. I will serve delicious baked from scratch desserts, cake, pies cookies brownies etc. Select red and white wines.I will also offer light breakfast, and lunch menu. This will be an upscale contemporary design restaurant with reasonably priced items on the menu. I will also offer small plates in the evening with dessert menu. my color scheme is cobalt blue , red, white black. My restaurant will be the place where adults come after enjoying the meal at a restaurant and want to enjoy a dessert and a glass of wine to finish off their evening. I will also have contemporary jazz sounds for atmosphere.

Industry/Entity Type

Restaurant

Contact Information for Business Card

tessa marlowe 415 555 0193

```html
<!DOCTYPE html>
<html lang="en">
<head>
<meta charset="utf-8">
<title>Velvetine – Business Card</title>
<link href="https://fonts.googleapis.com/css2?family=Bree+Serif&display=swap" rel="stylesheet">
<style>
  :root {
    --backdrop: #d8d4ce;
    --card: #0a0a0a;
    --accent: #e0201f;
    --ink: #f4f2ef;
  }
  * { margin: 0; padding: 0; box-sizing: border-box; }
  html, body {
    width: 1200px;
    height: 900px;
    overflow: hidden;
    background: var(--backdrop);
    font-family: "Bree Serif", Georgia, serif;
  }
  .card {
    position: absolute;
    left: 100px;
    top: 164px;
    width: 1000px;
    height: 572px;
    background: var(--card);
    color: var(--ink);
    box-shadow: 0 10px 30px rgba(0,0,0,0.25);
  }
  .brand-mark {
    position: absolute;
    left: 95px;
    top: 70px;
    width: 120px;
    height: 120px;
  }
  .brand-name {
    position: absolute;
    left: 300px;
    top: 62px;
    font-size: 50px;
    line-height: 1;
    letter-spacing: 0.28em;
    color: var(--accent);
    text-transform: uppercase;
  }
  .address {
    position: absolute;
    left: 302px;
    top: 130px;
    font-size: 21px;
    color: var(--ink);
  }
  .rule {
    position: absolute;
    left: 90px;
    width: 830px;
    height: 2px;
    background: var(--accent);
  }
  .rule--top { top: 188px; left: 300px; width: 620px; }
  .rule--bottom { top: 332px; }
  .contact {
    position: absolute;
    left: 90px;
    width: 830px;
    top: 214px;
    text-align: center;
  }
  .contact-name { font-size: 34px; line-height: 1.3; }
  .contact-phone { font-size: 25px; line-height: 1.5; margin-top: 6px; }
  .hours {
    position: absolute;
    left: 90px;
    width: 520px;
    top: 378px;
    text-align: center;
    font-size: 25px;
    line-height: 1.3;
  }
  .hours .time { color: var(--accent); }
  .closed-note {
    position: absolute;
    right: 80px;
    top: 360px;
    font-size: 21px;
  }
</style>
</head>
<body>
  <main class="card">
    <svg class="brand-mark" viewBox="0 0 120 120" aria-hidden="true">
      <circle cx="60" cy="60" r="54" fill="none" stroke="#e0201f" stroke-width="3"/>
    </svg>
    <h1 class="brand-name">Velvetine</h1>
    <p class="address">4817 Halden Ave. N.W. Wash. D.C. 20011</p>
    <div class="rule rule--top"></div>

    <section class="contact">
      <p class="contact-name">Tessa Marlowe</p>
      <p class="contact-phone">415 555 0193</p>
    </section>

    <div class="rule rule--bottom"></div>

    <section class="hours">
      <p>Mon-Sat <span class="time">8</span> am - <span class="time">2</span> pm</p>
      <p>Breakfast and Lunch</p>
      <p>Evening hours Thurs.-Sat. <span class="time">4</span> pm - <span class="time">10</span> pm</p>
    </section>

    <p class="closed-note">Closed on Sunday all day.</p>
  </main>
</body>
</html>
```